Business card for communications

Need a business card for my consulting business - I work with not for profits, start ups and social enterprises on their media, communications campaigns.

Please see my website for colours, images and fonts www.morvenquillet.example

Morven Quillet
Communications & Campaign strategist
Sydney - Melbourne
M: 0498 317 250
E: morven@morvenquillet.example
S: morvenquillet
W: morvenquillet.example
T: @morvenquillet

(above is info only and can be presented any way e.g. should not have to be M for mobile - it should be an icon)
Updates

Dear designers I have updated the brief and uploaded high res images from my website for you to use. The designs so far with the use of images and icons are much better so far. Thank you I look forward to receiving your revised designs. Morven Quillet

Industry/Entity Type

Communications

Font styles to use
Sans Serif

Requirements
Must have
• Icons for contact details
Images from the website www.morvenquillet.example
Nice to have
• Images - attached

```html
<!DOCTYPE html>
<html lang="en">
<head>
<meta charset="utf-8">
<title>Morven Quillet — Business Card</title>
<link rel="stylesheet" href="https://fonts.googleapis.com/css2?family=Hind:wght@400;500;600&display=swap">
<style>
  :root {
    --page: #ffffff;
    --card-orange: #f7a03e;
    --card-orange-deep: #ec9232;
    --ink-blue: #1d1fa6;
    --accent-green: #3f9c1c;
    --rule: #b9772c;
    --photo-wood: #b8742e;
    --photo-navy: #2d3350;
    --photo-light: #d9c7ad;
  }
  * { box-sizing: border-box; margin: 0; padding: 0; }
  html, body {
    width: 1200px; height: 900px; overflow: hidden;
    background: var(--page);
    font-family: "Hind", Arial, sans-serif;
    color: var(--ink-blue);
  }
  .canvas { position: relative; width: 1200px; height: 900px; }
  .card {
    position: absolute; top: 344px; width: 502px; height: 277px;
    border-radius: 20px; overflow: hidden;
    background:
      radial-gradient(circle at 20% 30%, rgba(200,120,40,.25), transparent 40%),
      radial-gradient(circle at 70% 80%, rgba(200,120,40,.2), transparent 35%),
      radial-gradient(circle at 85% 25%, rgba(255,190,110,.25), transparent 40%),
      var(--card-orange);
  }
  .card--back { left: 68px; }
  .card--front { left: 633px; }

  .contact {
    position: absolute; display: flex; align-items: center; gap: 10px;
    font-size: 12.5px; letter-spacing: 1.6px; white-space: nowrap;
  }
  .contact--tight { letter-spacing: .4px; }
  .icon { width: 24px; height: 24px; flex: none; }
  .rule-h { position: absolute; left: 30px; top: 148px; width: 440px; height: 1px; background: var(--rule); }
  .rule-v { position: absolute; left: 250px; top: 128px; width: 1px; height: 36px; background: var(--rule); }
  .role {
    position: absolute; left: 267px; top: 156px;
    font-size: 14px; font-weight: 500; letter-spacing: 1.8px; line-height: 22px;
  }
  .role .amp { color: var(--accent-green); font-weight: 600; }

  .photo {
    position: absolute; left: 0; top: 0; width: 100%; height: 201px;
    background:
      radial-gradient(ellipse at 30% 15%, var(--photo-navy), transparent 30%),
      radial-gradient(ellipse at 88% 15%, var(--photo-navy), transparent 25%),
      radial-gradient(ellipse at 55% 55%, var(--photo-light), transparent 35%),
      linear-gradient(180deg, #8c6a48 0%, var(--photo-wood) 45%, #a8672a 100%);
  }
  .name {
    position: absolute; left: 30px; top: 208px; line-height: 1;
  }
  .name__first { display: block; color: var(--accent-green); font-size: 17px; letter-spacing: 3.2px; }
  .name__last { display: block; color: var(--ink-blue); font-size: 20px; font-weight: 500; letter-spacing: 3.4px; margin-top: 3px; }
  .front-rule { position: absolute; left: 200px; top: 216px; width: 1px; height: 30px; background: var(--rule); }
  .front-role { position: absolute; left: 229px; top: 206px; }
  .front-role__top { display: block; font-size: 15.5px; font-weight: 500; letter-spacing: 1.6px; }
  .front-role__bottom { display: block; font-size: 12.5px; letter-spacing: 2.6px; margin-top: 4px; }
  .front-role__bottom .amp { color: var(--accent-green); font-weight: 600; }
</style>
</head>
<body>
<main class="canvas">

  <section class="card card--back" aria-label="Card back: contact details">
    <div class="contact contact--tight" style="left:30px;top:94px;">
      <svg class="icon" viewBox="0 0 24 24"><circle cx="12" cy="12" r="11" fill="var(--ink-blue)"/><rect x="6" y="8" width="12" height="8" fill="none" stroke="#f7a03e" stroke-width="1.4"/><path d="M6 8l6 5 6-5" fill="none" stroke="#f7a03e" stroke-width="1.4"/></svg>
      <span>morven@morvenquillet.example</span>
    </div>
    <div class="contact" style="left:30px;top:120px;">
      <svg class="icon" viewBox="0 0 24 24"><circle cx="12" cy="12" r="11" fill="var(--ink-blue)"/></svg>
      <span>morvenquillet</span>
    </div>
    <div class="contact" style="left:30px;top:152px;">
      <svg class="icon" viewBox="0 0 24 24"><circle cx="12" cy="12" r="11" fill="var(--ink-blue)"/></svg>
      <span>@morvenquillet</span>
    </div>
    <div class="contact contact--tight" style="left:30px;top:178px;">
      <svg class="icon" viewBox="0 0 24 24"><circle cx="12" cy="12" r="11" fill="var(--ink-blue)"/><text x="12" y="16.5" text-anchor="middle" font-size="13" fill="#f7a03e" font-family="Hind, sans-serif">@</text></svg>
      <span>morvenquillet.example</span>
    </div>

    <div class="rule-h"></div>
    <div class="rule-v"></div>

    <div class="contact" style="left:266px;top:92px;letter-spacing:2.6px;">
      <svg class="icon" viewBox="0 0 24 24"><circle cx="12" cy="12" r="11" fill="var(--ink-blue)"/><path d="M12 5.5a4 4 0 0 0-4 4c0 3 4 8 4 8s4-5 4-8a4 4 0 0 0-4-4z" fill="none" stroke="#f7a03e" stroke-width="1.4"/><circle cx="12" cy="9.5" r="1.4" fill="#f7a03e"/></svg>
      <span>Sydney-Melborn</span>
    </div>
    <div class="contact" style="left:266px;top:118px;letter-spacing:3px;">
      <svg class="icon" viewBox="0 0 24 24"><circle cx="12" cy="12" r="11" fill="var(--ink-blue)"/><rect x="8.5" y="5.5" width="7" height="13" rx="1.2" fill="none" stroke="#f7a03e" stroke-width="1.4"/><circle cx="12" cy="16.3" r=".8" fill="#f7a03e"/></svg>
      <span>0498 317 250</span>
    </div>

    <p class="role">Communication <span class="amp">&amp;</span><br>Campaign Strategist</p>
  </section>

  <section class="card card--front" aria-label="Card front">
    <div class="photo" role="img" aria-label="Overhead photo of a team working at a wooden desk with laptops, papers and plants"></div>
    <h1 class="name"><span class="name__first">MORVEN</span><span class="name__last">QUILLET</span></h1>
    <div class="front-rule"></div>
    <p class="front-role">
      <span class="front-role__top">Communication</span>
      <span class="front-role__bottom"><span class="amp">&amp;</span>Campaign Strategist</span>
    </p>
  </section>

</main>
</body>
</html>
```